Fahrzeugbeschriftung für Montage-Firma mit Jungem Team
Zielgruppe
Wir machen Montagen, Wartungen, Reparaturen von Tore Türen Fenster Böden. Zielgruppe sind Privatkunden und Firmenkunden
Aufgabenstellung
Es sollen die Farben vom Logo auf dem Design verwendet werden

```html
<!DOCTYPE html>
<html lang="de">
<head>
<meta charset="utf-8">
<title>Mandelborn Montage-Service – Fahrzeugbeschriftung</title>
<link href="https://fonts.googleapis.com/css2?family=Montserrat:wght@700;800&display=swap" rel="stylesheet">
<style>
  :root {
    --brand-blue: #2b4a72;
    --brand-grey: #6f6f70;
    --dark-grey: #3b3d41;
    --white: #ffffff;
    --paper: #f2f3f4;
  }
  * { margin: 0; padding: 0; box-sizing: border-box; }
  html, body { width: 1200px; height: 900px; overflow: hidden; background: var(--white); }
  body { font-family: 'Montserrat', Arial, sans-serif; }

  .wrap-layout {
    position: relative;
    width: 1200px;
    height: 900px;
    background: var(--paper);
  }

  .brand-block {
    position: absolute;
    left: 0; right: 0;
    top: 210px;
    display: flex;
    align-items: center;
    justify-content: center;
    gap: 22px;
  }
  .brand-square {
    width: 64px; height: 64px;
    background: var(--brand-blue);
  }
  .brand-name {
    font-weight: 800;
    font-size: 96px;
    letter-spacing: 2px;
    color: var(--brand-blue);
    line-height: 1;
  }

  .band-blue {
    position: absolute;
    left: 0; right: 0;
    top: 360px; height: 190px;
    background: var(--brand-blue);
    display: flex;
    flex-direction: column;
    align-items: center;
    justify-content: center;
    gap: 22px;
  }
  .tagline {
    display: flex;
    align-items: center;
    gap: 18px;
    color: var(--brand-grey);
    font-weight: 800;
    font-size: 36px;
    letter-spacing: 9px;
  }
  .tagline-rule {
    width: 150px; height: 4px;
    background: var(--brand-grey);
  }
  .services {
    color: var(--white);
    font-weight: 700;
    font-size: 32px;
    letter-spacing: 5px;
  }

  .stripe-grey {
    position: absolute;
    left: 0; right: 0;
    top: 570px; height: 26px;
    background: var(--brand-grey);
  }
  .band-dark {
    position: absolute;
    left: 0; right: 0;
    top: 660px; height: 80px;
    background: var(--dark-grey);
  }
</style>
</head>
<body>
  <main class="wrap-layout">
    <div class="brand-block">
      <span class="brand-square"></span>
      <span class="brand-name">MANDELBORN</span>
    </div>

    <section class="band-blue">
      <div class="tagline">
        <span class="tagline-rule"></span>
        <span>MONTAGE-SERVICE</span>
        <span class="tagline-rule"></span>
      </div>
      <div class="services">TORE-TÜREN-FENSTER-BÖDEN</div>
    </section>

    <div class="stripe-grey"></div>
    <div class="band-dark"></div>
  </main>
</body>
</html>
```